BRVL Brochure Design

Northfield Council of Clinical Standards (BRVL) needs a whole new brochure. I've upload EPS logos and past brochures. Our tagline is to "modernize healthcare" and we think our brochure should reflect that, so that's the purpose of this project.

BRVL is a proven leader in healthcare education, training and
consulting services for health professionals. We’ve earned a reputation for excellence in healthcare quality improvement and management.

BRVL works to improve healthcare quality by educating healthcare professionals about healthcare best practices. We focus on instructing our clients on how to plan for, measure, and improve healthcare quality in all facilities and facets such as:

Patient Safety
Infection Control
Performance Improvement
Risk Management
Compliance and Accreditation
Health and Hospital Administration
Health Insurance
Healthcare Financial Management
Facility Management and Safety

DESIGN SUGGESTIONS:

Brochure Size: 8.5 X 11 full size brochure or 8.5 X 11 trifold brochure

Number of Pages: 2 to 3

Colors: Feel free to use a wide array of colors but try to stay away from colors that are too loud, ex: Pink, Purple, Neon Green.

Themes: Professional, Educational

Designs:

Pelor by Oskar Lindqvist

Quorvo Pamphlet by Derek Malloway

Lanterns for harvest by Solvendri

Paisaje de Sr KT by vrpl

http://www.plimbask.com/post/28461937205/10-creative-brochure-designs

Don't limit yourself to these examples. However, these are examples we liked

Reason: We would like to see more designs

We want more full page designs than tri-fold 

We are considering both tri-fold and full-page but would like to see more full page designs 

Reason: Our lead designer making the decisions on this project has been fired. I apologize for the inconvenience. We want extend the project one last time

Target Market(s)

Students, Doctors, and Educational Professionals

Industry/Entity Type

Healthcare

Logo Text

asdfasdf

Font styles to use
Serif
Sans Serif
Decorative
Script

Requirements
Should not have
• Pink, Purple, Neon Green colors

```html
<!DOCTYPE html>
<html lang="en">
<head>
<meta charset="utf-8">
<title>BRVL Brochure – Mission and Course Offerings</title>
<link rel="stylesheet" href="https://fonts.googleapis.com/css2?family=Open+Sans:wght@400;700&family=Arimo:wght@400;700&family=Roboto+Slab:wght@700&display=swap">
<style>
  :root {
    --teal: #3ab0c3;
    --slate: #5b626b;
    --ink: #111416;
    --body: #3a3d40;
    --paper: #ffffff;
    --photo-light: #e6e6e6;
    --photo-mid: #a9a9a9;
    --photo-dark: #555;
  }
  * { box-sizing: border-box; margin: 0; padding: 0; }
  html, body { width: 1200px; height: 849px; overflow: hidden; background: var(--paper); }
  .spread { position: relative; width: 1200px; height: 849px; font-family: "Arimo", Arial, sans-serif; }
  .page { position: absolute; top: 0; height: 849px; }
  .page--left { left: 0; width: 596px; background: var(--slate); border-right: 1px solid #3f444a; }
  .page--right { left: 597px; width: 603px; background: var(--paper); }
  .block { position: absolute; }
  .tab { position: absolute; background: var(--teal); }
  .photo { position: absolute; }
  .photo--consult { left: 293px; top: 95px; width: 260px; height: 337px; background: linear-gradient(120deg, var(--photo-light), var(--photo-mid) 60%, var(--photo-dark)); }
  .photo--doctor { left: 45px; top: 432px; width: 248px; height: 351px; background: linear-gradient(160deg, #f0f0f0, #cfcfcf 55%, #8d8d8d); }
  .photo--patient { left: 0; top: 93px; width: 594px; height: 310px; background: linear-gradient(100deg, #8a8a8a, #d3d3d3 40%, #9a9a9a 70%, #e4e4e4); }

  .mission { left: 45px; top: 95px; width: 248px; height: 337px; background: var(--teal); padding: 16px 14px; }
  .mission h2 { font-family: "Open Sans", sans-serif; font-weight: 700; font-size: 19px; color: var(--ink); margin-bottom: 8px; }
  .mission p { font-family: "Arimo", sans-serif; font-weight: 700; font-size: 12.3px; line-height: 17.5px; color: var(--ink); }

  .values { left: 293px; top: 432px; width: 260px; height: 351px; background: var(--teal); padding: 4px 10px 0 18px; color: #222; }
  .values h2 { font-family: "Open Sans", sans-serif; font-weight: 700; font-size: 21px; color: var(--ink); margin: 0 0 8px 7px; }
  .values p { font-size: 9.2px; line-height: 11.3px; margin-bottom: 11px; }
  .values ul { list-style: none; margin-left: -8px; }
  .values li { font-size: 9.2px; line-height: 11.3px; margin-bottom: 12px; padding-left: 8px; position: relative; }
  .values li::before { content: ""; position: absolute; left: 0; top: 2px; width: 6px; height: 6px; background: var(--ink); }

  .offerings-title { position: absolute; left: 41px; top: 410px; font-family: "Open Sans", sans-serif; font-weight: 700; font-size: 21px; color: var(--teal); letter-spacing: 0.2px; }
  .offerings-sub { position: absolute; left: 41px; top: 437px; font-family: "Roboto Slab", serif; font-weight: 700; font-size: 11.5px; color: #555; letter-spacing: 0.3px; }

  .col { position: absolute; top: 480px; font-size: 9.3px; line-height: 11.3px; color: var(--body); }
  .col--intro { left: 41px; width: 160px; }
  .col--details { left: 219px; width: 160px; line-height: 14.3px; }
  .col--topics { left: 391px; width: 165px; line-height: 13.8px; }
  .col h3 { display: inline; font-family: "Open Sans", sans-serif; font-size: 12px; font-weight: 700; color: var(--ink); }
  .col h3.stand { display: block; margin-top: 14px; }
  .col .para { margin-bottom: 12px; }
  .sq-list { list-style: none; }
  .sq-list li { position: relative; padding-left: 7px; }
  .sq-list li::before { content: ""; position: absolute; left: 0; top: 4px; width: 5px; height: 5px; background: var(--teal); }
  .col--intro .sq-list li::before { left: -10px; }
  .col--intro .sq-list { margin-left: 0; }
  .note { color: var(--teal); font-style: italic; }
</style>
</head>
<body>
<main class="spread">
  <section class="page page--left">
    <div class="tab" style="left:44px;top:59px;width:42px;height:25px"></div>
    <div class="block mission">
      <h2>ABOUT US /MISSION</h2>
      <p>Our mission is to enhance quality in healthcare by transforming the professionals who work in healthcare. We aim to give you the tools and knowledge that you need to impact healthcare delivery and outcomes and to be an advocate for quality and patient safety.</p>
    </div>
    <div class="photo photo--consult" role="img" aria-label="Black and white photo of a smiling doctor showing a tablet to a patient"></div>
    <div class="photo photo--doctor" role="img" aria-label="Black and white photo of a doctor in a white coat holding a clipboard"></div>
    <div class="block values">
      <h2>OUR VALUES</h2>
      <p>If you're a healthcare professional or organization seeking top-notch professional development services, you've found what you're looking for. Consider BRVL's offerings:</p>
      <ul>
        <li>Our workshops and seminars address teambuilding, leadership, quality assurance and improvement, accreditation, performance measurement, patient safety, risk management, utilization management, hospital surveying, customer service, standards and communication, strategic planning, applied research, survey design and methods, re-engineering, and the Six Sigma management method.</li>
        <li>Our national and international conferences on quality management attract audiences of more than 1,000 of the world's leading health professionals.</li>
        <li>Our seminars cover cost benefit and effectiveness analysis, managed care, and medical informatics.</li>
        <li>Our consultants are always available to assess your needs and develop custom solutions for your facility.</li>
      </ul>
    </div>
    <div class="tab" style="left:273px;top:783px;width:50px;height:57px"></div>
  </section>

  <section class="page page--right">
    <div class="tab" style="left:508px;top:59px;width:42px;height:25px"></div>
    <div class="photo photo--patient" role="img" aria-label="Black and white photo of an older man with glasses comforted by a woman"></div>
    <h1 class="offerings-title">COURSE OFFERINGS</h1>
    <p class="offerings-sub">CERTIFICATE IN HEALTHCARE QUALITY (CHQ)</p>

    <div class="col col--intro">
      <p>The CHQ course is designed to give an in-depth but more generalized understanding of healthcare quality and its implementation. This course takes you through an overview of the healthcare systems in the US and a comparative study of other systems around the world, the concept of and principles of healthcare quality, and a history of how Quality has</p>
      <ul class="sq-list">
        <li style="padding-left:0">become an integral part of evaluating our healthcare system.</li>
        <li style="padding-left:0">Participants will hone their skills in organizational development, healthcare quality management, team building, problem solving techniques, and process improvement. By the end of this course, you will have learned how to assess, measure, and plan for, and improve quality within your healthcare organization.</li>
      </ul>
    </div>

    <div class="col col--details">
      <p class="para"><h3>Audience:</h3> This course is designed for the general healthcare professional without or with limited background in healthcare quality.</p>
      <p class="para" style="margin-top:12px"><h3>Prerequisite:</h3> Candidates for the CHQ course must be employed by a healthcare related entity, completed a bachelor is degree in a health related field or they must have extensive experience in healthcare at the managerial level.</p>
      <h3 class="stand" style="margin-top:14px">Topics Include:</h3>
      <ul class="sq-list">
        <li>Overview of the healthcare systems around the world</li>
        <li>Current issues of healthcare quality</li>
        <li>The Concept of healthcare quality</li>
        <li>Historical evolution of quality in healthcare</li>
      </ul>
    </div>

    <div class="col col--topics">
      <ul class="sq-list">
        <li>Planning and organizing for healthcare quality</li>
        <li>Quality improvement and quality assurance</li>
        <li>Dissemination of healthcare quality</li>
        <li>Data collection, analysis and management</li>
        <li>Measuring and monitoring quality</li>
        <li>Quality cost and cost containment Economics of healthcare quality Regulations, Accreditations, and Licensure</li>
      </ul>
      <h3 class="stand" style="margin-top:14px">Course information:</h3>
      <p><span class="note">Materials:</span> All materials are covered in the course fee<br><span class="note">Duration:</span> 32 hours</p>
    </div>
    <div class="tab" style="left:271px;top:783px;width:50px;height:57px"></div>
  </section>
</main>
</body>
</html>
```